依頼詳細
今回依頼するのは、500mlのビンの外箱です。

ビンの形状はワインボトルに似ています。

■依頼するビンの外箱のサイズは 高さ30cm×横7cm×奥行7cm の 細長い四角柱型。
■4面の中でデザイン箇所は、3面。1面は成分表示やお召し上がり方を記載します。
■ターゲットは20代~30代の女性向け
■商品の品質には絶対の自信があります。
■商品名は「ソフィレア」 Sofirea
■ダイエット効果や、美容、健康に重点を置いた商品なので、デザインイメージは「美しい女性」。

記載項目
特に無し。
希望イメージ
シンプル 複雑
単色 カラフル
暗い 明るい
日常 高級
遊び心 厳粛
未来的 伝統的
女性的 男性的
希望する色
ゴールド、グリーン、シルバーなど。単色でもOK。
納品ファイル
• 高解像度JPG (.jpg)
• イラストレーター形式 (.ai)
補足説明
ビンのイメージを追加します。

色は水色で、形状は画像のものとほぼ同じです。ご参考までに・・。
■ 選んだ理由

素晴らしいデザインで、社内の中でも満場一致です!

■ 提案者全員のお礼・コメント

皆様、本当にありがとうございました。

初めての依頼でしたので、お時間を頂きましたが、大満足でした。

また是非ご参加をお待ちしております。

```html
<!DOCTYPE html>
<html lang="ja">
<head>
<meta charset="utf-8">
<title>Sofirea 酵素ドリンク 外箱</title>
<link rel="stylesheet" href="https://fonts.googleapis.com/css2?family=Arimo:wght@700&family=Shippori+Mincho:wght@400;500&display=swap">
<style>
  :root {
    --teal-deep: #2fb3b6;
    --teal-mid: #6fd0cf;
    --teal-pale: #d6f1f0;
    --white: #ffffff;
    --gold: #b8923a;
    --gold-light: #e3cf8f;
    --ink: #3b4f52;
    --ink-soft: #6d8184;
    --water-a: #9fd6ea;
    --water-b: #cdeaf3;
  }
  * { margin: 0; padding: 0; box-sizing: border-box; }
  html, body { width: 679px; height: 1200px; overflow: hidden; background: var(--white); }
  .box-face {
    position: relative;
    width: 679px;
    height: 1200px;
    overflow: hidden;
    background: linear-gradient(180deg, var(--teal-deep) 0%, var(--teal-mid) 35%, var(--teal-pale) 62%, var(--white) 80%);
  }
  .top-band {
    position: absolute; left: 0; top: 0; width: 679px; height: 208px;
    background: linear-gradient(180deg, var(--white) 0%, var(--teal-pale) 45%, var(--teal-mid) 100%);
  }
  .center-strip {
    position: absolute; left: 252px; top: 0; width: 188px; height: 1200px;
    background: linear-gradient(180deg, var(--white) 0%, var(--white) 30%, rgba(255,255,255,0.85) 60%, rgba(255,255,255,0) 85%);
  }
  .gold-rule {
    position: absolute; left: 0; width: 679px; height: 4px;
    background: linear-gradient(90deg, var(--gold) 0%, var(--gold-light) 50%, var(--gold) 100%);
  }
  .gold-rule--top { top: 200px; }
  .gold-rule--mid { top: 520px; height: 3px; }
  .brand-name {
    position: absolute; left: 0; width: 679px; text-align: center;
    font-family: "Arimo", "Helvetica Neue", sans-serif; font-weight: 700;
    color: var(--gold); letter-spacing: 1px; line-height: 1;
  }
  .brand-name--top { top: 40px; font-size: 54px; }
  .brand-name--main { top: 412px; font-size: 54px; }
  .category {
    position: absolute; left: 328px; top: 232px;
    writing-mode: vertical-rl;
    font-family: "Shippori Mincho", serif; font-size: 20px; line-height: 1;
    color: var(--ink-soft); letter-spacing: 4px;
  }
  .splash-circle {
    position: absolute; left: 340px; top: 530px; width: 420px; height: 230px;
    border-radius: 50%; background: rgba(255,255,255,0.85);
  }
  .splash {
    position: absolute; left: 0; top: 585px; width: 679px; height: 110px;
    background: linear-gradient(90deg, rgba(159,214,234,0.55) 0%, rgba(120,190,225,0.6) 55%, rgba(205,234,243,0.4) 100%);
  }
  .ring-lines {
    position: absolute; left: 0; top: 760px; width: 679px; height: 440px;
  }
  .description {
    position: absolute; left: 0; top: 880px; width: 679px; text-align: center;
    font-family: "Shippori Mincho", serif; font-size: 16px; line-height: 44px;
    color: var(--ink);
  }
  .volume {
    position: absolute; left: 0; top: 1090px; width: 679px; text-align: center;
    font-family: "Shippori Mincho", serif; font-size: 34px; color: var(--ink);
  }
</style>
</head>
<body>
<main class="box-face">
  <div class="top-band"></div>
  <div class="center-strip"></div>
  <div class="gold-rule gold-rule--top"></div>

  <h1 class="brand-name brand-name--top">Sofirea</h1>
  <p class="category">酵素ドリンク</p>
  <p class="brand-name brand-name--main">Sofirea</p>

  <div class="gold-rule gold-rule--mid"></div>

  <div class="splash-circle"></div>
  <div class="splash" role="img" aria-label="澄んだ水が横に流れ、水滴が跳ねる写真"></div>

  <svg class="ring-lines" viewBox="0 0 679 440" aria-hidden="true">
    <g fill="none" stroke="#ffffff" stroke-width="1.5">
      <circle cx="339" cy="150" r="150"/>
      <circle cx="480" cy="230" r="170"/>
    </g>
  </svg>

  <p class="description">
    約100種類の野菜を発酵させ、<br>
    栄養分だけを抽出し、<br>
    酵母や酵素の働きで熟成発酵させた<br>
    複合植物エキス
  </p>

  <p class="volume">500㎖</p>
</main>
</body>
</html>
```